Short fill E liquid label UK. 100ml Nicotine free

Short Fill e liquid label (UK). The BRAND name is "Lumora" (Logo uploaded).Looking to release a new range under the Lumora name. The new range will be called "Spliced". A range of Liquids mixed together. Needs to look cool, stand out and funky but not too crazy. The range will have 10 different flavours so will need these all done, a simple flavour name towards bottom of label will do for this or a different colour for each.Any warnings ( requirements by law) etc and company address/details etc need to have a place on the labels. Basically need to be E liquid compliant label but all are nicotine free so not so many law requirements.Label Size will be 120mm( wide)x 60mm(high), bottle diameter is 41mm .

The 10 flavour names are as follows so will need appropriate colours for each flavour:
Berserker ( a menthol and custard mix )
Fruit loop ( a mixed fruit mix )
Smooth custard ( custard based mix )
Strawberry Shake ( Strawberry milkshake mix )
Cookie Jar ( a cookie based mix )
Black ice ( a liquorice and menthol mix )
Madagascan breeze ( Mainly vanilla based mix )
Choc shake ( chocolate milkshake )
nutter ( a peanut butter and banana mix )
Cool currant ( blackcurrant and menthol mix )

Requirements
Must have
• The info and warnings that need to be on the bottle are as follows:
• signs that need to be on bottle:
• 18+ sign
• Caution sign (!)
• United kingdom flag with" made in the united kingdom written underneath"
• text that needs to be on the bottle:
• Nicotine free eliquid. (in bold lettering )
• Keep out of the reach of children. Always
• read the label before use.
• If swallowed consult a doctor if feeling unwell . In case of contact with eyes consult a doctor.
• Dispose of in a responsible manner.
• Store in a dark place at room temperature.
• Ingredients:
• Vegetable glycerin, Propylene glycol, Flavourings.
• PG/VG ratio 70/30 %

```html
<!DOCTYPE html>
<html lang="en">
<head>
<meta charset="utf-8">
<title>Lumora Spliced – Smooth Custard Label</title>
<link rel="stylesheet" href="https://fonts.googleapis.com/css2?family=Lato:wght@400;700;900&display=swap">
<style>
  :root {
    --page: #e9e9ea;
    --label-dark: #0b0b0b;
    --label-mid: #1d1d1d;
    --ink-light: #ffffff;
    --ink-soft: #e8e8e8;
    --flavour: #f3e36a;
    --flavour-edge: #e4c441;
    --box: #ffffff;
    --box-ink: #111111;
  }
  * { box-sizing: border-box; margin: 0; padding: 0; }
  html, body {
    width: 850px; height: 1200px; overflow: hidden;
    background: var(--page);
    font-family: "Lato", Arial, sans-serif;
  }
  .canvas { position: relative; width: 850px; height: 1200px; }
  .label {
    position: absolute; left: 35px; top: 405px;
    width: 780px; height: 390px;
    background:
      linear-gradient(118deg, transparent 38%, rgba(255,255,255,0.06) 48%, transparent 58%),
      linear-gradient(160deg, var(--label-mid), var(--label-dark) 70%);
    box-shadow: 8px 10px 14px rgba(0,0,0,0.35);
    color: var(--ink-light);
    overflow: hidden;
  }
  .block { position: absolute; text-align: center; transform: translateX(-50%); }
  .heading { font-weight: 700; font-size: 15.5px; white-space: nowrap; }
  .copy { font-size: 13px; line-height: 1.3; color: var(--ink-soft); }
  .copy.small { font-size: 11.5px; }
  .nicotine { font-weight: 900; font-size: 16px; white-space: nowrap; }

  .warn-heading { left: 130px; top: 36px; }
  .warn-swallow { left: 130px; top: 72px; width: 186px; }
  .warn-dispose { left: 130px; top: 160px; width: 180px; }
  .warn-store { left: 130px; top: 209px; width: 180px; }

  .best-before {
    position: absolute; left: 33px; top: 251px; width: 197px; height: 31px;
    background: var(--box); color: var(--box-ink);
    font-size: 12px; font-style: italic; font-weight: 700;
    padding: 8px 0 0 12px;
  }
  .flag { position: absolute; left: 34px; top: 297px; width: 83px; height: 49px; display: block; }
  .origin-text { left: 180px; top: 303px; font-size: 13.5px; line-height: 1.2; color: var(--ink-soft); white-space: nowrap; }

  .brand-tab { left: 390px; top: 0; width: 130px; height: 135px; display: flex; align-items: center; justify-content: center; }
  .brand-name { font-weight: 900; font-size: 30px; color: var(--ink-light); }

  .range-name { left: 390px; top: 168px; font-weight: 900; font-size: 64px; line-height: 1; letter-spacing: 1px; color: var(--ink-light); }
  .range-sub { left: 390px; top: 257px; font-weight: 900; font-size: 12.5px; letter-spacing: 3.2px; color: var(--ink-soft); white-space: nowrap; }
  .flavour-icon {
    left: 390px; top: 282px; width: 44px; height: 32px;
    background: linear-gradient(var(--flavour), var(--flavour-edge));
    border-radius: 6px 6px 3px 3px;
  }
  .flavour-name {
    left: 390px; top: 326px; white-space: nowrap;
    border: 2px solid var(--flavour);
    padding: 1px 8px; font-weight: 900; font-size: 15px; color: var(--flavour);
  }

  .ingr-heading { left: 650px; top: 38px; }
  .ingr-copy { left: 650px; top: 70px; width: 236px; }
  .nicotine-line { left: 650px; top: 135px; }
  .children { left: 650px; top: 178px; width: 220px; }

  .signs { position: absolute; left: 652px; top: 219px; display: flex; gap: 16px; align-items: center; transform: translateX(-50%); }
  .age-badge {
    width: 50px; height: 50px; border-radius: 50%; background: var(--box); color: var(--box-ink);
    display: flex; align-items: center; justify-content: center; font-weight: 900; font-size: 22px;
  }
  .caution { width: 56px; height: 50px; display: block; }
  .barcode-slot {
    position: absolute; left: 562px; top: 288px; width: 180px; height: 65px;
    background: var(--box); color: var(--box-ink);
    display: flex; align-items: center; justify-content: center; font-size: 24px;
  }
</style>
</head>
<body>
<div class="canvas">
  <section class="label">
    <p class="block heading warn-heading">Read the label before use.</p>
    <p class="block copy warn-swallow">If swallowed consult a doctor if feeling unwell . In case of contact with eyes consult a doctor.</p>
    <p class="block copy warn-dispose">Dispose of in a responsible manner.</p>
    <p class="block copy warn-store">Store in a dark place at room temperature.</p>
    <div class="best-before">Best Before:</div>
    <svg class="flag" viewBox="0 0 60 36" aria-label="United Kingdom flag" role="img">
      <rect width="60" height="36" fill="#012169"/>
      <path d="M0,0 L60,36 M60,0 L0,36" stroke="#fff" stroke-width="7"/>
      <path d="M0,0 L60,36 M60,0 L0,36" stroke="#c8102e" stroke-width="2.5"/>
      <path d="M30,0 V36 M0,18 H60" stroke="#fff" stroke-width="11"/>
      <path d="M30,0 V36 M0,18 H60" stroke="#c8102e" stroke-width="6.5"/>
    </svg>
    <p class="block origin-text">Made in the<br>united kingdom</p>

    <div class="block brand-tab"><span class="brand-name">Lumora</span></div>
    <p class="block range-name">SPLICED</p>
    <p class="block range-sub">E-CIGARETTES &amp; LIQUID</p>
    <span class="block flavour-icon" role="img" aria-label="Custard pudding icon"></span>
    <span class="block flavour-name">SMOOTH CUSTARD</span>

    <p class="block heading ingr-heading">ingredients:</p>
    <p class="block copy ingr-copy">Vegetable glycerin, Propylene glycol,<br>Flavourings.<br>PG/VG ratio 70/30 %</p>
    <p class="block nicotine nicotine-line">Nicotine free eliquid.</p>
    <p class="block copy small children">Keep out of the reach of children.<br>Always</p>
    <div class="signs">
      <div class="age-badge">18+</div>
      <svg class="caution" viewBox="0 0 56 50" role="img" aria-label="Caution">
        <path d="M28,4 L53,47 H3 Z" fill="none" stroke="#fff" stroke-width="3.5" stroke-linejoin="round"/>
        <rect x="26" y="17" width="4" height="17" fill="#fff"/>
        <circle cx="28" cy="40" r="2.6" fill="#fff"/>
      </svg>
    </div>
    <div class="barcode-slot">bar code</div>
  </section>
</div>
</body>
</html>
```